Business card for Kestrel Bathrooms

Please design a business card for our bathroom renovation business. You can use my existing logo, but if you have an idea to modernize it, I would like to see it. Please see attached files first. I would like to use the blue and the orange theme. I like the concept of using the shower head in the logo. Please find following a design (or two) that I have been trying to create with my limited resources. That design was for a sign, but I was going to adopt it and use it as a business card as well. I like the concept of the water splash but I don’t think it “flows” nicely together with the logo. Another thought is that maybe creating the logo out of water splash could work and have a dramatic effect (like the water text and the butterfly picture attached with similar background instead of white). If the above doesn’t work I would like to see a modern simplified design. One of the attached files named as the unwanted business card has all the details that I want included in the business card. Please note that it is two sided.
Updates

I am very thankful for the designs that I have received, but they are very similar and only a couple of attempts to do something with the water splash as per my original brief. Modernizing the logo and having it made out of out of water splash with the orange as color accent could work and have a dramatic effect (like the water text and the butterfly picture attached with similar background instead of white). Please do not use the butterfly itself! This is just an example that images can be created out of water splash.

Contact Information for Business Card

all the details are on the unwonted business card file included

Colors
3176b5

Requirements
Nice to have
• Copied from the brief:
• ... maybe creating the logo out of water splash could work and have a dramatic effect (like the water text and the butterfly picture attached with similar background instead of white). Please do not use the butterfly itself!
Should not have
• I am getting designs with a butterfly. The butterfly picture was an example of creating something from a water splash. The butterfly itself has no association with anything other than the concept of creating a logo out of water splash. Sorry, I thought I was clear in the brief.

```html
<!DOCTYPE html>
<html lang="en">
<head>
<meta charset="utf-8">
<title>Kestrel Bathrooms – Business Card</title>
<link href="https://fonts.googleapis.com/css2?family=Roboto:wght@400;500;700&family=Patrick+Hand&display=swap" rel="stylesheet">
<style>
  :root {
    --page: #e4e4e4;
    --navy: #1b2f52;
    --navy-deep: #152644;
    --splash-light: #b9c3d2;
    --white: #ffffff;
    --coral: #ea7462;
  }
  * { box-sizing: border-box; margin: 0; padding: 0; }
  html, body {
    width: 1200px; height: 960px; overflow: hidden;
    background: var(--page);
    font-family: "Roboto", Arial, sans-serif;
    color: var(--white);
  }
  .card {
    position: absolute;
    width: 600px; height: 343px;
    background: var(--navy);
    overflow: hidden;
  }
  .card--back { left: 302px; top: 124px; }
  .card--front { left: 299px; top: 493px; }

  .splash {
    position: absolute;
    opacity: .75;
  }
  .card--back .splash {
    left: 0; top: 40px; width: 280px; height: 303px;
    background:
      radial-gradient(ellipse 55% 60% at 35% 75%, rgba(185,195,210,.55), transparent 70%),
      radial-gradient(ellipse 40% 50% at 10% 95%, rgba(185,195,210,.45), transparent 70%);
  }
  .card--front .splash {
    left: 320px; top: 0; width: 280px; height: 343px;
    background:
      radial-gradient(ellipse 45% 55% at 45% 70%, rgba(185,195,210,.5), transparent 70%),
      radial-gradient(ellipse 35% 45% at 90% 40%, rgba(185,195,210,.35), transparent 70%);
  }

  .services {
    position: absolute; right: 42px; top: 70px;
    list-style: none; text-align: right;
    font-size: 15px; line-height: 24px;
  }
  .services li::after {
    content: ""; display: inline-block;
    width: 6px; height: 6px; border-radius: 50%;
    background: var(--coral);
    margin-left: 9px; vertical-align: middle;
  }

  .memberships { position: absolute; left: 377px; top: 260px; display: flex; align-items: center; gap: 28px; }
  .badge { background: var(--white); }
  .badge--round { width: 32px; height: 34px; border-radius: 6px 6px 14px 14px; }
  .badge--wide { width: 118px; height: 24px; border-radius: 2px; }

  .brand { position: absolute; left: 118px; top: 42px; display: flex; align-items: center; gap: 12px; }
  .brand__mark { width: 16px; height: 16px; border-radius: 50%; background: var(--coral); }
  .brand__name { font-weight: 500; color: var(--white); line-height: 1; }
  .brand__name .line1 { display: block; font-size: 52px; }
  .brand__name .line2 { display: block; font-size: 22px; letter-spacing: 4px; margin-top: 6px; }

  .person {
    position: absolute; left: 31px; top: 172px;
    font-family: "Patrick Hand", cursive;
    font-size: 25px; color: var(--coral);
  }
  .contacts { position: absolute; left: 31px; top: 209px; list-style: none; font-size: 17px; line-height: 21.5px; }
  .contacts li { display: flex; align-items: center; gap: 7px; }
  .contacts svg { width: 14px; height: 14px; flex: none; }
  .contacts .phones { font-weight: 700; font-size: 18px; margin-bottom: 1px; }
  .contacts .sep { margin: 0 12px; font-weight: 400; }
  .abn { position: absolute; left: 50px; top: 307px; font-size: 10px; }
</style>
</head>
<body>

<section class="card card--back">
  <div class="splash" role="img" aria-label="Photographic water splash rising from the lower left"></div>
  <ul class="services">
    <li>Complete Bathroom Renovations &amp; Remodelling</li>
    <li>Professional Service From Concept To Completion</li>
    <li>Highly Skilled &amp; Qualified Tradespeople</li>
    <li>All Work Guaranteed</li>
  </ul>
  <div class="memberships">
    <div class="badge badge--round" role="img" aria-label="Industry association membership badge"></div>
    <div class="badge badge--wide" role="img" aria-label="Builders association membership badge"></div>
  </div>
</section>

<section class="card card--front">
  <div class="splash" role="img" aria-label="Photographic water splash on the right side"></div>
  <div class="brand">
    <span class="brand__name"><span class="line1">Kestrel</span><span class="line2">Bathrooms</span></span>
    <span class="brand__mark"></span>
  </div>
  <p class="person">Liam Carvossa</p>
  <ul class="contacts">
    <li class="phones">
      <svg viewBox="0 0 24 24" fill="var(--coral)"><path d="M6.6 10.8a15 15 0 0 0 6.6 6.6l2.2-2.2a1 1 0 0 1 1-.25 11.4 11.4 0 0 0 3.6.57 1 1 0 0 1 1 1V20a1 1 0 0 1-1 1A17 17 0 0 1 3 4a1 1 0 0 1 1-1h3.5a1 1 0 0 1 1 1c0 1.25.2 2.45.57 3.57a1 1 0 0 1-.25 1z"/></svg>
      <span>0400 555 217<span class="sep">|</span>6200 4418</span>
    </li>
    <li>
      <svg viewBox="0 0 24 24" fill="none" stroke="var(--coral)" stroke-width="2.4"><circle cx="12" cy="12" r="4"/><path d="M16 8v5a3 3 0 0 0 6 0v-1a10 10 0 1 0-4 8"/></svg>
      <span>liam@kestrelbathrooms.com.au</span>
    </li>
    <li>
      <svg viewBox="0 0 24 24" fill="none" stroke="var(--coral)" stroke-width="2.2"><circle cx="12" cy="12" r="9.5"/><path d="M2.5 12h19M12 2.5c3 3 3 16 0 19M12 2.5c-3 3-3 16 0 19"/></svg>
      <span>kestrelbathrooms.com.au</span>
    </li>
    <li>
      <svg viewBox="0 0 24 24" fill="var(--coral)"><path d="M2 5h20v14H2z"/><path d="M2 5l10 8 10-8" fill="none" stroke="var(--navy)" stroke-width="2"/></svg>
      <span>PO Box 81 Larkfield 2620</span>
    </li>
  </ul>
  <p class="abn">ABN 12 345 678 901</p>
</section>

</body>
</html>
```